IT services web page design

Hello!

We need new design for our web site, obviously :)

Our company is service oriented and we are maintaining, configuring and fixing problems for IT + selling other internet related services.

Our speciality are in area of internet services (web, dns, email, databases, backup...) and internet servers technology.

We also provide service and sales of Zentro Apps and Veltrania Quillbox365 for which we are certified by Zentro and Veltrania.

Other services that we provide (not so in focus) are: VPS hosting, remote backup, web hosting, pagemoss fixing...

People mostly call us when they have a problems and this is core idea that new web site has to communicate - We can fix your server / web / email problems, save your money and as* :)

Our team have 15+ years experience with all range of internet technology + bunch of certificates from Veltrania and Durvo [we need to show people we have certificates].
Our qualities: experience, knowledge, delivery on time

In start we will not have blog section, but we need it in future. We also need place for flonkit feeds on web site.

Depth of the site should be max. level 2.

This site will go out in two languages so we need switch button on page from pone language to another.

Target Market(s)

small and mid size business that use internet services for daily operations and main business

Industry/Entity Type

Internet

Requirements
Must have
• * design should be in the way that responsive web could be made

Nice to have
• Long format will be OK for us. Like today pages that list all services and benefits on one loooong web page...

Logo is in attachment. It will be nice to have it on web site but if you find it not appropriate you can change it or put another one.

```html
<!DOCTYPE html>
<html lang="en">
<head>
<meta charset="utf-8">
<title>Corvane Group – IT &amp; Internet Services</title>
<link rel="stylesheet" href="https://fonts.googleapis.com/css2?family=Open+Sans:wght@300;400;600;700&family=Roboto+Condensed:wght@700&display=swap">
<style>
:root{
  --ink:#2b2b2b;
  --muted:#555;
  --blue:#1f8fd0;
  --blue-deep:#0b4f80;
  --blue-dark:#0a3e68;
  --hero-top:#2f9ee0;
  --hero-bottom:#0a4a7d;
  --topbar:#1a1a1a;
  --grey-band:#eef0f0;
  --card-line:#d6d6d6;
  --footer:#4a4a4a;
  --footer-text:#d9d9d9;
  --base:#1f1f1f;
  --white:#ffffff;
}
*{box-sizing:border-box;margin:0;padding:0}
html,body{width:1200px;height:3400px;overflow:hidden}
body{font-family:"Open Sans",Arial,sans-serif;color:var(--ink);background:var(--white);position:relative}
a{color:inherit;text-decoration:none}

/* top bar */
.topbar{height:52px;background:var(--topbar);display:flex;align-items:center;padding:0 24px;color:var(--white)}
.brand{font-size:26px;font-weight:700;letter-spacing:2px;color:var(--white)}
.topbar-links{margin-left:auto;display:flex;gap:30px;font-size:13px;align-items:center}
.lang-switch{background:var(--white);color:var(--ink);font-size:12px;padding:3px 10px;width:64px;border:1px solid #999}

/* hero */
.hero{height:628px;background:linear-gradient(var(--hero-top),var(--hero-bottom));color:var(--white);text-align:center;position:relative}
.main-nav{position:absolute;right:70px;top:60px;display:flex;gap:0;font-size:14px}
.main-nav a{padding:10px 28px}
.main-nav a.is-active{border-bottom:2px solid var(--white)}
.main-nav-line{position:absolute;left:385px;right:60px;top:108px;border-top:1px solid rgba(255,255,255,.4)}
.hero-kicker{padding-top:188px;font-size:20px;font-weight:600;letter-spacing:1px;color:#0b2336}
.hero-title{font-size:40px;font-weight:700;margin-top:2px}
.hero-sub{font-size:20px;margin-top:14px;line-height:1.35}
.hero-devices{position:absolute;left:255px;top:378px;width:720px;height:500px;border-radius:8px;background:linear-gradient(#2b2b2b,#0b0b0b 70%,#cfd3d6);}

/* about */
.about{padding:264px 75px 0;text-align:center}
.section-title{font-size:30px;font-weight:300;color:var(--blue);letter-spacing:1px}
.body-copy{font-size:13px;line-height:1.6;color:var(--muted);margin-top:18px}

/* services */
.services{position:absolute;top:1190px;left:0;width:1200px;height:560px;background:linear-gradient(var(--grey-band) 0 190px,var(--white) 190px)}
.services .section-title{color:#777;font-size:28px;text-align:center;margin-top:66px}
.services-rule{width:1050px;margin:26px auto 0;border-top:1px solid var(--card-line)}
.service-grid{position:absolute;top:160px;left:24px;display:flex;gap:46px}
.service-card{width:154px;height:210px;background:var(--white);border:1px solid var(--card-line);text-align:center;font-size:15px;color:#555;position:relative}
.service-card svg{display:block;margin:24px auto 12px}
.service-card.is-active{background:var(--blue-dark);color:var(--white);border-color:var(--blue-dark)}
.service-card.is-active::after{content:"";position:absolute;left:63px;bottom:-16px;border:14px solid transparent;border-top-color:var(--blue-dark);border-bottom:0}
.service-detail{position:absolute;top:408px;left:24px;width:390px;font-size:13px;line-height:1.6;color:var(--muted)}

/* testimonials */
.testimonials{position:absolute;top:1760px;left:0;width:1200px;height:470px;border-top:1px solid #e2e2e2;text-align:center}
.testimonials .section-title{margin-top:54px;font-size:32px}
.slider-arrow{position:absolute;top:170px;width:72px;height:72px;border-radius:50%;background:#e6eaee;display:flex;align-items:center;justify-content:center}
.slider-arrow.prev{left:20px}.slider-arrow.next{right:20px}
.client-photo{width:110px;height:110px;border-radius:50%;margin:28px auto 0;background:radial-gradient(#7a5a45,#3a2a22);border:4px solid #ddd}
.client-name{font-size:14px;font-style:italic;margin-top:20px;color:var(--ink)}
.testimonials .body-copy{padding:0 75px;margin-top:40px}

/* expertise */
.expertise{position:absolute;top:2248px;left:0;width:1200px;height:597px;background:linear-gradient(90deg,#f2f2f2,#d9dadb)}
.expertise-lead{position:absolute;left:195px;top:160px;font-size:46px;font-weight:300;color:#333}
.expertise-sub{position:absolute;left:258px;top:220px;font-size:31px;font-weight:300;color:var(--blue)}
.expertise-copy{position:absolute;left:135px;top:280px;width:420px;font-size:20px;line-height:1.35;text-align:center;color:#333}
.cta-button{position:absolute;left:195px;top:400px;width:285px;height:62px;border-radius:6px;background:linear-gradient(#2f77ad,#0c3f6b);color:var(--white);font-family:"Roboto Condensed",Arial,sans-serif;font-size:25px;display:flex;align-items:center;justify-content:center}
.hand-device{position:absolute;left:650px;top:40px;width:400px;height:557px;border-radius:40px 40px 0 0;background:linear-gradient(#e8e8e8,#bfa08a)}
.whys-panel{position:absolute;left:700px;top:130px;width:248px;height:310px;background:var(--white);border:1px solid #aaa}
.whys-panel h3{background:#bdbdbd;font-size:18px;text-align:center;padding:10px 0;color:#333}
.whys-panel ul{list-style:none;padding:14px 12px}
.whys-panel li{font-size:13px;display:flex;align-items:center;gap:10px;margin-bottom:14px;color:#333}

/* footer */
.footer{position:absolute;top:2845px;left:0;width:1200px;height:495px;background:var(--footer);color:var(--footer-text);font-size:12px}
.footer-col{position:absolute;top:56px}
.footer-col h4{font-size:14px;font-weight:400;letter-spacing:1px;margin-bottom:30px}
.footer-col ul{list-style:none;line-height:1.6}
.feed{display:flex;gap:14px;margin-bottom:26px;width:220px}
.feed-dot{flex:0 0 32px;height:32px;border-radius:50%;background:var(--white)}
.feed p{line-height:1.45}
.feed em{display:block;margin-top:4px}
.feed em span,.blog-post a,.contact-line span{color:var(--blue)}
.blog-post{width:230px;margin-bottom:26px;line-height:1.45}
.blog-post h5{color:var(--blue);font-size:13px;font-weight:600;margin-bottom:8px}
.contact-block{line-height:1.5}
.follow{color:var(--blue);font-size:18px;margin-top:44px}
.social{display:flex;gap:12px;margin-top:14px}
.social span{width:40px;height:40px;border-radius:50%;background:var(--white)}
.base{position:absolute;top:3340px;left:0;width:1200px;height:60px;background:var(--base);color:var(--footer-text);font-size:14px;display:flex;align-items:center;justify-content:center}
</style>
</head>
<body>

<header class="topbar">
  <span class="brand">CORVANE GROUP</span>
  <nav class="topbar-links">
    <a href="#">Help Desk</a>
    <a href="#">Login</a>
    <a href="#">Register</a>
    <span class="lang-switch">English ▾</span>
  </nav>
</header>

<section class="hero">
  <nav class="main-nav">
    <a class="is-active" href="#">HOME</a>
    <a href="#">ABOUT US</a>
    <a href="#">SERVICES</a>
    <a href="#">PARTNERS</a>
    <a href="#">BLOG</a>
    <a href="#">CONTACT US</a>
  </nav>
  <div class="main-nav-line"></div>
  <p class="hero-kicker">CORVANE GROUP</p>
  <h1 class="hero-title">PROVID THE BEST IT  AND INTERNET SERVICES</h1>
  <p class="hero-sub">We are Spelist in Maintaining ,configuring and<br>Fixing the It and Internet services</p>
  <div class="hero-devices" role="img" aria-label="Desktop monitor, tablet and laptop showing the company name, with a cloud and check mark"></div>
</section>

<section class="about">
  <h2 class="section-title">ABOUT CORVANE</h2>
  <p class="body-copy">Lorem Ipsum is simply dummy text of the printing and typesetting industry. Lorem Ipsum has been the industry's standard dummy text ever since the 1500s, when an unknown printer took a galley of type and scrambled it to make a type specimen book. It has survived not only five centuries, but also the leap into electronic typesetting, remaining essentially unchanged. It was popularised in the 1960s with the release of Lettrix sheets containing Lorem Ipsum passages, and more recently with desktop publishing software like Quarrel PageForge including versions of Lorem Ipsum.</p>
</section>

<section class="services">
  <h2 class="section-title">SERVICES WE PROVIDE</h2>
  <div class="services-rule"></div>
  <div class="service-grid">
    <div class="service-card is-active">
      <svg width="100" height="100" viewBox="0 0 100 100"><circle cx="50" cy="50" r="46" fill="none" stroke="#fff" stroke-width="4"/><rect x="28" y="32" width="44" height="28" fill="#fff"/><rect x="44" y="62" width="12" height="6" fill="#fff"/><rect x="36" y="68" width="28" height="3" fill="#fff"/></svg>
      Web<br>Services
    </div>
    <div class="service-card">
      <svg width="100" height="100" viewBox="0 0 100 100"><circle cx="50" cy="50" r="46" fill="none" stroke="#1f6fae" stroke-width="4"/><circle cx="50" cy="50" r="20" fill="none" stroke="#1f6fae" stroke-width="3"/><ellipse cx="50" cy="50" rx="9" ry="20" fill="none" stroke="#1f6fae" stroke-width="3"/><line x1="30" y1="50" x2="70" y2="50" stroke="#1f6fae" stroke-width="3"/></svg>
      DNS<br>Services
    </div>
    <div class="service-card">
      <svg width="100" height="100" viewBox="0 0 100 100"><circle cx="50" cy="50" r="46" fill="none" stroke="#1f6fae" stroke-width="4"/><path d="M28 36h16l4 5h24v26H28z" fill="#1f6fae"/></svg>
      Database<br>Services
    </div>
    <div class="service-card">
      <svg width="100" height="100" viewBox="0 0 100 100"><circle cx="50" cy="50" r="46" fill="none" stroke="#1f6fae" stroke-width="4"/><rect x="28" y="36" width="44" height="28" rx="3" fill="#1f6fae"/><circle cx="41" cy="48" r="5" fill="#fff"/><circle cx="59" cy="48" r="5" fill="#fff"/></svg>
      Back up<br>Services
    </div>
    <div class="service-card">
      <svg width="100" height="100" viewBox="0 0 100 100"><circle cx="50" cy="50" r="46" fill="none" stroke="#1f6fae" stroke-width="4"/><rect x="38" y="26" width="24" height="46" rx="5" fill="none" stroke="#1f6fae" stroke-width="4"/><circle cx="50" cy="65" r="2.5" fill="#1f6fae"/></svg>
      Application<br>Services
    </div>
    <div class="service-card">
      <svg width="100" height="100" viewBox="0 0 100 100"><circle cx="50" cy="50" r="46" fill="none" stroke="#1f6fae" stroke-width="4"/><rect x="36" y="26" width="28" height="48" rx="3" fill="#1f6fae"/><line x1="40" y1="36" x2="60" y2="36" stroke="#fff" stroke-width="2"/><line x1="40" y1="44" x2="60" y2="44" stroke="#fff" stroke-width="2"/><line x1="40" y1="52" x2="60" y2="52" stroke="#fff" stroke-width="2"/></svg>
      Web<br>Hosting
    </div>
  </div>
  <p class="service-detail">Website Design,  Website Redesign, Website Maintenance, Flash Web Design, Custom Web Design, Web 2.0 Development, Custom Web Development, E-commerce Web Development, Content Management Syste</p>
</section>

<section class="testimonials">
  <h2 class="section-title">What Our Clients Say About US</h2>
  <a class="slider-arrow prev" href="#" aria-label="Previous"><svg width="20" height="24" viewBox="0 0 20 24"><path d="M15 3 5 12l10 9" fill="none" stroke="#333" stroke-width="4"/></svg></a>
  <a class="slider-arrow next" href="#" aria-label="Next"><svg width="20" height="24" viewBox="0 0 20 24"><path d="M5 3l10 9-10 9" fill="none" stroke="#333" stroke-width="4"/></svg></a>
  <div class="client-photo" role="img" aria-label="Portrait of client Renna Oakley"></div>
  <p class="client-name">Renna Oakley  ( fernlightstudio.net )</p>
  <p class="body-copy">Lorem Ipsum is simply dummy text of the printing and typesetting industry. Lorem Ipsum has been the industry's standard dummy text ever since the 1500s, when an unknown printer took a galley of type and scrambled it to make a type specimen book. It has survived not only five centuries, but also the leap into electronic typesetting, remaining essentially unchanged. It was popularised in the 1960s with the release of Lettrix sheets containing Lorem Ipsum passages, and more recently with desktop publishing software like Quarrel PageForge including versions of Lorem Ipsum</p>
</section>

<section class="expertise" role="img" aria-label="Faint mosaic of team member portraits behind the section">
  <p class="expertise-lead">WE ARE</p>
  <p class="expertise-sub">TEAM OF EXPERT</p>
  <p class="expertise-copy">Team of Hard Worker have 15+ year experience with all range of internet  Technology + Bunch of Certificate from Veltrania and Durvo.</p>
  <a class="cta-button" href="#">CONTACT US NOW</a>
  <div class="hand-device" role="img" aria-label="Hand holding a tablet"></div>
  <div class="whys-panel">
    <h3>WHYS US</h3>
    <ul>
      <li><svg width="18" height="18" viewBox="0 0 18 18"><rect x="1" y="1" width="16" height="16" fill="#c9d07a" stroke="#777"/><path d="M4 9l3 3 7-7" fill="none" stroke="#333" stroke-width="2"/></svg>Lorem Ipsum is simply dummy</li>
      <li><svg width="18" height="18" viewBox="0 0 18 18"><rect x="1" y="1" width="16" height="16" fill="#c9d07a" stroke="#777"/><path d="M4 9l3 3 7-7" fill="none" stroke="#333" stroke-width="2"/></svg>Lorem Ipsum is simply dummy</li>
      <li><svg width="18" height="18" viewBox="0 0 18 18"><rect x="1" y="1" width="16" height="16" fill="#c9d07a" stroke="#777"/><path d="M4 9l3 3 7-7" fill="none" stroke="#333" stroke-width="2"/></svg>Lorem Ipsum is simply dummy</li>
      <li><svg width="18" height="18" viewBox="0 0 18 18"><rect x="1" y="1" width="16" height="16" fill="#c9d07a" stroke="#777"/><path d="M4 9l3 3 7-7" fill="none" stroke="#333" stroke-width="2"/></svg>Lorem Ipsum is simply dummy</li>
      <li><svg width="18" height="18" viewBox="0 0 18 18"><rect x="1" y="1" width="16" height="16" fill="#c9d07a" stroke="#777"/><path d="M4 9l3 3 7-7" fill="none" stroke="#333" stroke-width="2"/></svg>Lorem Ipsum is simply dummy</li>
      <li><svg width="18" height="18" viewBox="0 0 18 18"><rect x="1" y="1" width="16" height="16" fill="#c9d07a" stroke="#777"/><path d="M4 9l3 3 7-7" fill="none" stroke="#333" stroke-width="2"/></svg>Lorem Ipsum is simply dummy</li>
    </ul>
  </div>
</section>

<footer class="footer">
  <div class="footer-col" style="left:24px">
    <h4>QUICK LINKS</h4>
    <ul><li>Home</li><li>About us</li><li>Sagone</li><li>Services</li><li>Clients</li><li>Privacy policy</li><li>Terms of use</li><li>Contact us</li></ul>
  </div>
  <div class="footer-col" style="left:330px">
    <h4>FLONKIT FEEDS</h4>
    <div class="feed"><span class="feed-dot"></span><p>info@mailvoro.net<br><br>Lorem Ipsum is simply dummy text of the printing and typesetting industry. Lorem Ipsum has been the industry's<em>Posted : <span>14 Hours Ago</span></em></p></div>
    <div class="feed"><span class="feed-dot"></span><p>info@mailvoro.net<br><br>Lorem Ipsum is simply dummy text of the printing and typesetting industry. Lorem Ipsum has been the industry's<em>Posted : <span>14 Hours Ago</span></em></p></div>
  </div>
  <div class="footer-col" style="left:628px">
    <h4>BLOG</h4>
    <div class="blog-post"><h5>Blog Headline Goes Here</h5>Lorem Ipsum is simply dummy text of the printing and typesetting industry. Lorem Ipsum has been the industry's standard dummy text ever since the 1500s, when an<br><br><a href="#">Read more</a></div>
    <div class="blog-post"><h5>Blog Headline Goes Here</h5>Lorem Ipsum is simply dummy text of the printing and typesetting industry. Lorem Ipsum has been the industry's standard dummy text ever since the 1500s, when an<br><br><a href="#">Read more</a></div>
  </div>
  <div class="footer-col" style="left:928px">
    <h4>CONTACT US</h4>
    <p class="contact-block">482 Alder Creek Rd<br>Maplewood, Ohio<br>40217, USA</p>
    <p class="contact-block contact-line" style="margin-top:26px">CALL US : <span>555-014-2290</span><br>EMAIL : <span>hello@corvane-mail.net</span></p>
    <p class="follow">FOLLOW US :</p>
    <div class="social"><span></span><span></span><span></span><span></span></div>
  </div>
</footer>
<div class="base">© 2013 Corvane Group, Inc. All rights reserved.</div>

</body>
</html>
```